Stationary Design Foundation Repair Business

We need business card and letterhead design for foundation repair business. Design must compliment the supplied logo. Font is eurostyle. please feel free to ask any questions. Also if we could incorporate the KTW file into the design, but keep the size of it small. Personal details are located in the stationary file.
Updates
I just uploaded a business card design that i like. Just so you guys know what my taste is. Is it possible to create something like this with my business card?
Target Market(s)
Home owners, Builders, Building surveyors, Insurance companies
Industry/Entity Type
Business
Other font styles liked:
- eurostile extended / bold
Look and feel

```html
<!DOCTYPE html>
<html lang="en">
<head>
<meta charset="utf-8">
<title>Deepfield Stationery Set</title>
<link href="https://fonts.googleapis.com/css2?family=Michroma&family=Play:wght@400;700&display=swap" rel="stylesheet">
<style>
:root{
  --bg:#6e6e6e;
  --paper:#ffffff;
  --ink:#1a1a1a;
  --red:#c4161c;
  --card:#0d0d0d;
  --faint:#f0f0f0;
  --seal:#d8d8d8;
  --seal-edge:#777777;
}
*{margin:0;padding:0;box-sizing:border-box}
html,body{width:1200px;height:1000px;overflow:hidden}
body{background:var(--bg);position:relative;font-family:"Play",sans-serif;color:var(--ink)}
.sheet{position:absolute;overflow:hidden}
.wave{position:absolute;left:0;bottom:0;width:100%;display:block}

.letterhead{left:35px;top:30px;width:595px;height:843px;background:var(--paper)}
.envelope{left:450px;top:160px;width:630px;height:290px;background:var(--paper);box-shadow:0 2px 8px rgba(0,0,0,.35)}
.card{background:var(--card)}
.card-front{left:752px;top:463px;width:390px;height:240px}
.card-back{left:748px;top:724px;width:390px;height:240px}

.brand{position:absolute}
.brand-name{font-family:"Michroma",sans-serif;font-size:19px;color:var(--ink);letter-spacing:.5px;display:flex;align-items:center;gap:8px;line-height:1;white-space:nowrap}
.brand-dot{width:13px;height:13px;border-radius:50%;background:var(--red);display:inline-block;flex:none}
.brand-tag{font-family:"Play",sans-serif;font-weight:700;font-size:7.5px;letter-spacing:1.4px;color:var(--red);text-transform:uppercase;margin-top:5px;padding-left:21px;white-space:nowrap}
.abn{font-size:10px;color:var(--ink);text-align:right;margin-top:6px}

.contacts{position:absolute;list-style:none;font-size:8.5px;line-height:11px;color:var(--ink);white-space:nowrap}
.contacts li{display:flex;align-items:flex-start;gap:5px}
.contacts .ic{width:7px;height:7px;background:var(--red);border-radius:1px;margin-top:2px;flex:none}

.seal{position:absolute;display:flex;align-items:center;gap:6px}
.seal-ring{width:24px;height:24px;border-radius:50%;border:2px solid var(--seal-edge);background:var(--seal)}
.seal-plate{width:70px;height:14px;border-radius:2px;background:var(--seal)}

.faint-name{position:absolute;font-family:"Michroma",sans-serif;color:var(--faint);white-space:nowrap}

.person{position:absolute;left:217px;top:30px}
.person-name{font-family:"Play",sans-serif;font-weight:700;font-size:15px;color:var(--red)}
.person-role{font-size:9px;color:#ddd;margin-top:5px}
.card .contacts{color:#eee}
.card .contacts .ic{background:#ddd}
.card .brand-name{color:#fff}
.card .seal-ring{border-color:#aaa;background:#333}
.card .seal-plate{background:#444}
.card-abn{position:absolute;left:83px;top:161px;font-size:11px;color:#fff}
</style>
</head>
<body>

<section class="sheet letterhead" aria-label="Letterhead">
  <div class="brand" style="left:40px;top:52px">
    <div class="brand-name"><span class="brand-dot"></span>DEEPFIELD</div>
    <div class="brand-tag">Professional Underpinning Services</div>
    <div class="abn">ABN: 12 345 678 901</div>
  </div>
  <div class="seal" style="left:441px;top:23px" role="img" aria-label="Registration badge">
    <span class="seal-ring"></span><span class="seal-plate"></span>
  </div>
  <ul class="contacts" style="left:441px;top:58px">
    <li><span class="ic"></span>0400 123 456</li>
    <li><span class="ic"></span>hello@deepfield.example</li>
    <li><span class="ic"></span>www.deepfield.example</li>
    <li><span class="ic"></span>12 Example Way Northvale<br>Vic 3000</li>
  </ul>
  <div class="faint-name" style="left:130px;top:440px;font-size:44px">DEEPFIELD</div>
  <svg class="wave" width="595" height="110" viewBox="0 0 595 110" preserveAspectRatio="none" aria-hidden="true">
    <path d="M0 28 C150 70 330 70 595 50 L595 110 L0 110Z" fill="var(--red)"/>
    <path d="M0 22 C150 64 330 64 595 44" fill="none" stroke="var(--ink)" stroke-width="4"/>
  </svg>
</section>

<section class="sheet envelope" aria-label="Envelope">
  <div class="brand" style="left:38px;top:38px">
    <div class="brand-name"><span class="brand-dot"></span>DEEPFIELD</div>
    <div class="brand-tag">Professional Underpinning Services</div>
    <div class="abn">ABN: 12 345 678 901</div>
  </div>
  <ul class="contacts" style="left:55px;top:118px">
    <li><span class="ic"></span>0400 123 456</li>
    <li><span class="ic"></span>hello@deepfield.example</li>
    <li><span class="ic"></span>www.deepfield.example</li>
    <li><span class="ic"></span>12 Example Way Northvale<br>Vic 3000</li>
  </ul>
  <div class="seal" style="left:62px;top:180px" role="img" aria-label="Registration badge">
    <span class="seal-ring"></span><span class="seal-plate"></span>
  </div>
  <div class="faint-name" style="left:290px;top:140px;font-size:30px">DEEPFIELD</div>
  <svg class="wave" width="630" height="90" viewBox="0 0 630 90" preserveAspectRatio="none" aria-hidden="true">
    <path d="M0 40 C180 80 380 70 520 35 C570 22 610 18 630 20 L630 90 L0 90Z" fill="var(--red)"/>
    <path d="M0 36 C180 76 380 66 520 31 C570 18 610 14 630 16" fill="none" stroke="var(--ink)" stroke-width="4"/>
  </svg>
</section>

<section class="sheet card card-front" aria-label="Business card front">
  <div class="brand" style="left:36px;top:100px">
    <div class="brand-name" style="font-size:17px"><span class="brand-dot"></span>DEEPFIELD</div>
  </div>
  <div class="person">
    <div class="person-name">Marco Belling</div>
    <div class="person-role">Proprietor</div>
  </div>
  <ul class="contacts" style="left:217px;top:128px;font-size:9px;line-height:15px">
    <li><span class="ic" style="margin-top:4px"></span>555.010.2020</li>
    <li><span class="ic" style="margin-top:4px"></span>hello@deepfield.example</li>
    <li><span class="ic" style="margin-top:4px"></span>www.deepfield.example</li>
    <li><span class="ic" style="margin-top:4px"></span>12 Example Way Northvale<br>Vic 3000</li>
  </ul>
  <svg class="wave" width="390" height="75" viewBox="0 0 390 75" preserveAspectRatio="none" aria-hidden="true">
    <path d="M0 8 C80 30 180 65 390 27 L390 75 L0 75Z" fill="var(--red)"/>
    <path d="M0 4 C80 26 180 61 390 23" fill="none" stroke="#fff" stroke-width="3"/>
  </svg>
</section>

<section class="sheet card card-back" aria-label="Business card back">
  <div class="brand" style="left:33px;top:68px">
    <div class="brand-name" style="font-size:19px"><span class="brand-dot"></span>DEEPFIELD</div>
    <div class="brand-tag" style="color:#fff">Professional Underpinning Services</div>
  </div>
  <div class="card-abn">ABN: 12 345 678 901</div>
  <div class="seal" style="left:218px;top:150px" role="img" aria-label="Registration badge">
    <span class="seal-ring" style="width:30px;height:30px"></span><span class="seal-plate" style="width:88px;height:16px"></span>
  </div>
  <svg class="wave" width="390" height="62" viewBox="0 0 390 62" preserveAspectRatio="none" aria-hidden="true">
    <path d="M0 8 C80 28 180 56 390 24 L390 62 L0 62Z" fill="var(--red)"/>
    <path d="M0 4 C80 24 180 52 390 20" fill="none" stroke="#fff" stroke-width="3"/>
  </svg>
</section>

</body>
</html>
```